brightwave pools cards

i need to create a design to use on my business cards,brochures and as a letterhead. i am a new swimming pool renovation business named BRIGHTWAVE POOLS. I require a smart professional deign to reflect that my business is the best in the industry.
should include something like.... Brightwave Pools ABN - 71508246913
residential pool renovation specialists
specialising in the art of - fully tiled pools
- waterline tiles
- natural stone pool copings
and outdoor areas - concrete slabs - detailed mosaic work - pool lighting and water features - pool painting

marcus - 0431928604 leonard -0467203851 brightwavepoolsco@tidelmail.com

the design could feature - water, natural stone (travertine, sandstone etc), something to personafy the word imagine.
looking foward to seeing some ideas... cheers heaps marcus

```html
<!DOCTYPE html>
<html lang="en">
<head>
<meta charset="utf-8">
<title>Brightwave Pools – Business Cards</title>
<link rel="stylesheet" href="https://fonts.googleapis.com/css2?family=Open+Sans:wght@400;600;700&display=swap">
<style>
  :root {
    --page-bg: #e9ebee;
    --card-bg: #ffffff;
    --brand-blue: #1b63ab;
    --brand-navy: #1d4f86;
    --ink: #3a3a3a;
    --tile-light: #bfe0f2;
    --tile-mid: #7fb6de;
    --tile-deep: #3f86c3;
    --card-shadow: 0 6px 18px rgba(0, 0, 0, 0.18);
  }
  * { box-sizing: border-box; margin: 0; padding: 0; }
  html, body {
    width: 1200px; height: 948px; overflow: hidden;
    background: var(--page-bg);
    font-family: "Open Sans", Verdana, sans-serif;
  }
  .canvas { position: relative; width: 1200px; height: 948px; }

  .card {
    position: absolute; width: 620px; height: 355px;
    background: var(--card-bg); box-shadow: var(--card-shadow);
    overflow: hidden;
  }
  .card--back { left: 80px; top: 90px; }
  .card--front { left: 500px; top: 500px; }
  .card__art { position: absolute; inset: 0; width: 100%; height: 100%; }

  /* back face */
  .services__title {
    position: absolute; left: 42px; top: 44px;
    font-size: 24px; font-weight: 700; color: var(--brand-blue);
  }
  .services__list {
    position: absolute; left: 48px; top: 94px; list-style: none;
  }
  .services__item {
    display: flex; align-items: center; gap: 12px;
    height: 27px; font-size: 15px; color: var(--brand-blue);
  }
  .services__tick { width: 16px; height: 16px; flex: none; }

  /* front face */
  .brand {
    position: absolute; left: 28px; top: 52px;
    display: flex; align-items: stretch;
  }
  .brand__name {
    font-size: 34px; font-weight: 700; color: var(--brand-navy);
    line-height: 1.2; white-space: nowrap; padding-right: 14px;
  }
  .brand__tagline {
    border-left: 2px solid var(--brand-blue); padding-left: 10px;
    font-size: 13px; font-weight: 700; color: var(--brand-blue);
    line-height: 1.3; letter-spacing: 0.3px;
  }
  .brand__licence {
    display: block; margin-top: 6px; font-weight: 400; font-style: italic;
    color: var(--ink); font-size: 12px;
  }
  .abn {
    position: absolute; left: 60px; top: 98px;
    font-size: 13px; color: var(--ink); letter-spacing: 0.3px;
  }
  .contacts {
    position: absolute; top: 158px; font-size: 13px; color: var(--ink);
    list-style: none;
  }
  .contacts--phones { left: 40px; }
  .contacts--online { left: 318px; color: var(--brand-blue); }
  .contacts__row { display: flex; align-items: center; gap: 8px; height: 22px; }
  .contacts__icon { width: 13px; height: 13px; flex: none; }
  .contacts__spacer { width: 13px; flex: none; }
</style>
</head>
<body>
<main class="canvas">

  <!-- back face: services -->
  <section class="card card--back" aria-label="Card back – services">
    <svg class="card__art" viewBox="0 0 620 355" preserveAspectRatio="none">
      <defs>
        <linearGradient id="tilesBack" x1="0" y1="0" x2="1" y2="1">
          <stop offset="0" stop-color="var(--tile-light)"/>
          <stop offset="0.5" stop-color="var(--tile-mid)"/>
          <stop offset="1" stop-color="var(--tile-deep)"/>
        </linearGradient>
      </defs>
      <path role="img" aria-label="Blue pool mosaic tile area"
            d="M0,312 C220,345 420,300 620,235 L620,355 L0,355 Z" fill="url(#tilesBack)"/>
      <path d="M0,308 C220,341 420,296 620,231" fill="none" stroke="var(--brand-blue)" stroke-width="9"/>
    </svg>
    <h2 class="services__title">Specialising In:</h2>
    <ul class="services__list">
      <li class="services__item"><svg class="services__tick" viewBox="0 0 16 16"><rect x="1" y="1" width="14" height="14" fill="none" stroke="var(--brand-blue)" stroke-width="1.6"/><path d="M4 8 l3 3 l6 -8" fill="none" stroke="var(--brand-blue)" stroke-width="2"/></svg>fully tiled pools</li>
      <li class="services__item"><svg class="services__tick" viewBox="0 0 16 16"><rect x="1" y="1" width="14" height="14" fill="none" stroke="var(--brand-blue)" stroke-width="1.6"/><path d="M4 8 l3 3 l6 -8" fill="none" stroke="var(--brand-blue)" stroke-width="2"/></svg>waterline tiles</li>
      <li class="services__item"><svg class="services__tick" viewBox="0 0 16 16"><rect x="1" y="1" width="14" height="14" fill="none" stroke="var(--brand-blue)" stroke-width="1.6"/><path d="M4 8 l3 3 l6 -8" fill="none" stroke="var(--brand-blue)" stroke-width="2"/></svg>pool copings and outdoor areas</li>
      <li class="services__item"><svg class="services__tick" viewBox="0 0 16 16"><rect x="1" y="1" width="14" height="14" fill="none" stroke="var(--brand-blue)" stroke-width="1.6"/><path d="M4 8 l3 3 l6 -8" fill="none" stroke="var(--brand-blue)" stroke-width="2"/></svg>concrete slabs</li>
      <li class="services__item"><svg class="services__tick" viewBox="0 0 16 16"><rect x="1" y="1" width="14" height="14" fill="none" stroke="var(--brand-blue)" stroke-width="1.6"/><path d="M4 8 l3 3 l6 -8" fill="none" stroke="var(--brand-blue)" stroke-width="2"/></svg>detailed mosaic work</li>
      <li class="services__item"><svg class="services__tick" viewBox="0 0 16 16"><rect x="1" y="1" width="14" height="14" fill="none" stroke="var(--brand-blue)" stroke-width="1.6"/><path d="M4 8 l3 3 l6 -8" fill="none" stroke="var(--brand-blue)" stroke-width="2"/></svg>pool lighting and water features</li>
      <li class="services__item"><svg class="services__tick" viewBox="0 0 16 16"><rect x="1" y="1" width="14" height="14" fill="none" stroke="var(--brand-blue)" stroke-width="1.6"/><path d="M4 8 l3 3 l6 -8" fill="none" stroke="var(--brand-blue)" stroke-width="2"/></svg>pool painting</li>
    </ul>
  </section>

  <!-- front face: brand and contacts -->
  <section class="card card--front" aria-label="Card front – contacts">
    <svg class="card__art" viewBox="0 0 620 355" preserveAspectRatio="none">
      <defs>
        <linearGradient id="tilesFront" x1="0" y1="0" x2="1" y2="1">
          <stop offset="0" stop-color="var(--tile-light)"/>
          <stop offset="0.5" stop-color="var(--tile-mid)"/>
          <stop offset="1" stop-color="var(--tile-deep)"/>
        </linearGradient>
      </defs>
      <path role="img" aria-label="Blue pool mosaic tile area"
            d="M0,238 C120,300 300,305 620,215 L620,355 L0,355 Z" fill="url(#tilesFront)"/>
      <path d="M0,234 C120,296 300,301 620,211" fill="none" stroke="var(--brand-blue)" stroke-width="9"/>
    </svg>

    <div class="brand">
      <span class="brand__name">Brightwave Pools</span>
      <p class="brand__tagline">Sydney's Pool<br>Renovation Specialists<span class="brand__licence">Lic- 318207D</span></p>
    </div>
    <p class="abn">ABN - 71508246913</p>

    <ul class="contacts contacts--phones">
      <li class="contacts__row">
        <svg class="contacts__icon" viewBox="0 0 16 16"><rect width="16" height="16" rx="2" fill="var(--ink)"/><path d="M5 3.5 l2 2.5 -1.2 1.2 c0.8 1.5 1.5 2.2 3 3 l1.2 -1.2 2.5 2 -1.5 1.8 c-4 -0.5 -7.3 -3.8 -7.8 -7.8 z" fill="#fff"/></svg>
        Marcus&nbsp;&nbsp;-0431928604
      </li>
      <li class="contacts__row"><span class="contacts__spacer"></span>Leonard -0467203851</li>
    </ul>

    <ul class="contacts contacts--online">
      <li class="contacts__row">
        <svg class="contacts__icon" viewBox="0 0 16 16"><rect x="1" y="3" width="14" height="10" fill="var(--brand-navy)"/><path d="M1.5 3.5 L8 9 L14.5 3.5" fill="none" stroke="#fff" stroke-width="1.3"/></svg>
        brightwavepoolsco@tidelmail.com
      </li>
      <li class="contacts__row">
        <svg class="contacts__icon" viewBox="0 0 16 16"><rect x="1" y="1" width="14" height="14" fill="var(--brand-navy)"/></svg>
        brightwavepools@wavepage.net
      </li>
    </ul>
  </section>

</main>
</body>
</html>
```